Medical program Vora produce by HALVOCARE

I need a business card of the program to give to the customer to get the general information to contact the clinic. I need a bilingual card French and English you will see the logo.
That's a program that the Clinic Halvocare offers. https://medicalvora.ca
Program: Vora Medical Program
Slogan: Lose weight - Exist - Live / Be light - Thrive - Live
The clinic that offers the program: Halvocare
Website: https://medicalvora.ca
---
Medical team / Medical team
email: doc@halvocare.ca
phone: 514 555-0148
Information
email: vora@halvocare.ca
phone: 514 555-0172 ext 3
Every person that needs to lose weight
Health clinic for obese person
All the information in the description
- Look clean - Expensive clinic / Need to be bilingual
- Recto verso for french and english

```html
<!DOCTYPE html>
<html lang="en">
<head>
<meta charset="utf-8">
<title>Vora Medical Program – Business Card</title>
<link rel="stylesheet" href="https://fonts.googleapis.com/css2?family=Montserrat:wght@400;500;700&family=Poppins:wght@700&display=swap">
<style>
  :root {
    --backdrop: #1c1c1e;
    --card: #0a0a0a;
    --blue: #0a84d0;
    --teal: #17a89a;
    --red: #d9313d;
    --white: #ffffff;
    --divider: #4a4a4a;
  }
  * { box-sizing: border-box; margin: 0; padding: 0; }
  html, body {
    width: 1200px; height: 900px; overflow: hidden;
    background: var(--backdrop);
  }
  .sheet {
    position: relative; width: 1200px; height: 900px;
    display: flex; flex-direction: column; align-items: center; justify-content: center;
    gap: 60px;
  }
  .card {
    position: relative; width: 600px; height: 343px;
    background: var(--card); border-radius: 22px; overflow: hidden;
    box-shadow: 0 10px 30px rgba(0,0,0,.45);
  }
  .band {
    position: absolute; left: 0; right: 0; top: 232px; height: 44px;
    display: flex; align-items: center; justify-content: center;
  }
  /* Front */
  .card--front .band { background: var(--blue); }
  .slogan {
    font-family: "Montserrat", sans-serif; font-weight: 500;
    font-size: 24px; color: var(--white); letter-spacing: .3px;
  }
  .program-name {
    position: absolute; left: 58px; top: 96px;
    display: flex; align-items: center; gap: 14px;
  }
  .program-name__dot {
    width: 26px; height: 26px; border-radius: 50%; background: var(--teal);
  }
  .program-name__text {
    font-family: "Montserrat", sans-serif; font-weight: 500;
    font-size: 64px; color: var(--teal); line-height: 1;
  }
  .divider {
    position: absolute; left: 300px; top: 48px; width: 1px; height: 160px;
    background: var(--divider);
  }
  .contacts {
    position: absolute; left: 326px; top: 52px;
    font-family: "Montserrat", sans-serif; color: var(--white);
  }
  .contact-group + .contact-group { margin-top: 16px; }
  .contact-group__title {
    font-weight: 700; font-size: 15px; letter-spacing: .3px; margin-bottom: 4px;
  }
  .contact-group--team .contact-group__title { color: var(--blue); }
  .contact-group--info .contact-group__title { color: var(--teal); }
  .contact-line {
    display: flex; align-items: center; gap: 8px;
    font-size: 15px; line-height: 22px;
  }
  .contact-line svg { width: 14px; height: 14px; flex: none; }
  .contact-group--team svg { fill: var(--blue); }
  .contact-group--info svg { fill: var(--teal); }
  /* Back */
  .card--back .band { background: var(--teal); justify-content: flex-end; padding-right: 70px; }
  .website {
    font-family: "Montserrat", sans-serif; font-weight: 500;
    font-size: 15px; color: var(--white);
  }
  .clinic-name {
    position: absolute; left: 0; right: 0; top: 86px;
    display: flex; flex-direction: column; align-items: center; gap: 18px;
  }
  .clinic-name__mark { width: 52px; height: 52px; background: var(--red); }
  .clinic-name__text {
    font-family: "Poppins", sans-serif; font-weight: 700;
    font-size: 50px; color: var(--white); letter-spacing: 1px; line-height: 1;
  }
</style>
</head>
<body>
<main class="sheet">
  <section class="card card--front" aria-label="Front of card">
    <div class="program-name">
      <span class="program-name__dot"></span>
      <span class="program-name__text">Vora</span>
    </div>
    <div class="divider"></div>
    <div class="contacts">
      <div class="contact-group contact-group--team">
        <p class="contact-group__title">MEDICAL TEAM</p>
        <p class="contact-line">
          <svg viewBox="0 0 16 16"><path d="M1 3h14v10H1z"/><path d="M1 3h14L8 9z" fill="#0a0a0a"/></svg>
          doc@halvocare.ca
        </p>
        <p class="contact-line">
          <svg viewBox="0 0 16 16"><path d="M3 1.5l3 3-1.6 1.8c.9 2 2.3 3.4 4.3 4.3L10.5 9l3 3-2 2.5C6 14 2 10 1.5 4.5z"/></svg>
          514 555-0148
        </p>
      </div>
      <div class="contact-group contact-group--info">
        <p class="contact-group__title">INFORMATION</p>
        <p class="contact-line">
          <svg viewBox="0 0 16 16"><path d="M1 3h14v10H1z"/><path d="M1 3h14L8 9z" fill="#0a0a0a"/></svg>
          vora@halvocare.ca
        </p>
        <p class="contact-line">
          <svg viewBox="0 0 16 16"><path d="M3 1.5l3 3-1.6 1.8c.9 2 2.3 3.4 4.3 4.3L10.5 9l3 3-2 2.5C6 14 2 10 1.5 4.5z"/></svg>
          514 555-0172 ext 3
        </p>
      </div>
    </div>
    <div class="band"><span class="slogan">Be light - Thrive - Live</span></div>
  </section>

  <section class="card card--back" aria-label="Back of card">
    <div class="clinic-name">
      <span class="clinic-name__mark"></span>
      <span class="clinic-name__text">HALVOCARE</span>
    </div>
    <div class="band"><span class="website">www.medicalvora.ca</span></div>
  </section>
</main>
</body>
</html>
```